Need some visual "dash" to a dashboard UI design

Have a project that needs a little visual "zip". Attached are some screenshots of the current design. Will need source files of design work, Photoshop preferred, but Illustrator or other source will be acceptable. Please confirm before starting the work.

Here is a working prototype:
https://pm47rd.vexolo.example/#g=1&p=scenario_1_-_dashboard_view

Work has been done to get the UI elements in place, but need a little visual improvement to make it really "pop" ...while retaining its usability.

Primarily need some visual design done for the left column 5 elements revealing values for tech in and tech out between 0 and 20. Auth OT values are 0min, 30min, 60min, 90min, 120min, and "over 2 hours". Avail Reserve Capacity will be 0% through 10%. And Supply Delta can range from -10,000 to +10,000

Some design for the charts on the right would be great. Just trying to establish a visual language to apply to these values.

Please use colors from the approved palette with hex values (plus black and white):

Primary
Orange ff7200
Orange Highlight fcb314
Blue 067ab4
Blue Highlight 3aa5dc

Secondary
Lime b6bf00
Lime Highlight dbd810
Green 6ebb1f
Green Highlight c4d82d
Burgundy b30a3c
Burgundy Highlight da3872
Purple 81017e
Purple Highlight b8509e
Dark Blue 0c2577
Dark Blue Highlight 020bb3

Accent
Ochre eaab00
Magenta ff0066
Royal Blue 000066
Yellow ffef00
Teal 00c7b2
Dusty Blue 96b1d0
Light Blue bcc9d6
Mint Green 99ffcc
Gold ff9900
Taupe cccc66
Warm Gray cccc99

• Must conform to the overall page layout described in the design doc attached. Must conform to the corporate color palette attached in the description.
• sorry, forgot to mention font: must use Verdana
• Verdana Font Family
• Verdana Regular
• Verdana Italic
• Verdana Bold
• Verdana Bold Italic

```html
<!DOCTYPE html>
<html lang="en">
<head>
<meta charset="utf-8">
<title>Capacity Dashboard</title>
<link href="https://fonts.googleapis.com/css2?family=Lato:wght@300;400;700&display=swap" rel="stylesheet">
<style>
:root{
  --orange:#ff7200; --orange-hl:#fcb314; --blue:#067ab4; --blue-hl:#3aa5dc;
  --green:#6ebb1f; --green-hl:#c4d82d; --burgundy:#b30a3c; --burgundy-hl:#da3872;
  --purple:#81017e; --purple-hl:#b8509e; --red:#cc0000;
  --ink:#333; --muted:#555; --soft:#888; --line:#ddd;
  --page:#2b2b2d; --canvas:#e9e9e9; --panel:#f2f2f2; --card:#fff;
}
*{box-sizing:border-box;margin:0;padding:0}
html,body{width:1200px;height:1200px;overflow:hidden;background:var(--page);font-family:'Lato',sans-serif;color:var(--ink)}
.app{position:absolute;left:0;top:183px;width:1200px;height:833px;background:var(--canvas)}
.abs{position:absolute}
.topbar{left:0;top:0;width:1200px;height:30px;background:var(--blue)}
.brand{left:24px;top:0;height:30px;display:flex;align-items:center;gap:5px;color:#fff;font-weight:700;font-size:11px}
.brand i{width:14px;height:14px;border-radius:50%;background:#fff;opacity:.85;display:block}
.tab-capacity{left:89px;top:0;width:61px;height:30px;background:var(--orange);color:#fff;font-size:8.5px;display:flex;align-items:center;justify-content:center;gap:4px}
.tab-more{left:160px;top:0;height:30px;color:#fff;font-size:8.5px;display:flex;align-items:center;gap:6px}
.tab-more span.dot{width:13px;height:13px;border:1px solid #fff;border-radius:50%;display:block}
.navbar{left:0;top:30px;width:1200px;height:37px;background:#fff;display:flex;align-items:center;font-size:11.5px;color:var(--muted)}
.nav-item{position:absolute;top:12px;display:flex;align-items:center;gap:5px}
.nav-item.active{color:var(--orange);font-size:14px;top:10px}
.icon-box{width:14px;height:14px;border:1px solid #888;display:inline-block;border-radius:2px}

.panel-left{left:20px;top:79px;width:366px;height:748px;background:var(--panel);box-shadow:0 1px 3px rgba(0,0,0,.15)}
.actions-label{left:5px;top:22px;font-size:12px;color:var(--muted)}
.select{left:72px;top:15px;width:279px;height:20px;border:1px solid #ccc;border-radius:10px;background:#fff;font-size:7.5px;padding:5px 13px;color:var(--muted)}
.select:after{content:"";position:absolute;right:10px;top:5px;width:5px;height:5px;border-right:1px solid #555;border-bottom:1px solid #555;transform:rotate(45deg)}
.pill{top:58px;height:34px;color:#fff;font-size:8.5px;display:flex;align-items:center;justify-content:center}
.days{top:100px;font-size:11px;color:var(--blue)}
.day-line{left:8px;top:130px;width:350px;height:1px;background:#ccc}
.day-ind{left:8px;top:128px;width:30px;height:3px;background:var(--orange-hl)}
.dates{top:136px;font-size:8.5px;color:var(--muted)}

.site{left:0;width:366px;height:80px}
.accent{left:0;top:0;width:6px;height:74px}
.site.closed .accent{background:var(--purple-hl)}
.site.open .accent{background:var(--green)}
.site-name{left:17px;top:0;font-size:17px;font-weight:300;color:var(--muted);letter-spacing:.3px}
.badge{left:288px;top:-2px;width:74px;height:24px;border-radius:12px;color:#fff;font-size:11.5px;display:flex;align-items:center;justify-content:center}
.closed .badge{background:var(--red)}
.open .badge{background:#22a012}
.metric{top:31px;height:41px;font-size:11.5px;text-align:center;color:var(--ink)}
.metric.boxed{background:#fff;border:1px solid #ddd}
.metric .sub{position:absolute;left:0;right:0;top:22px;font-size:9.5px;color:var(--muted);display:flex;align-items:center;justify-content:center;gap:3px}
.metric .title{position:absolute;left:0;right:0;top:4px}
.cap-bar{position:absolute;left:13px;top:30px;width:40px;height:7px;border:1px solid var(--blue);padding:1px}
.cap-bar i{display:block;height:100%;background:var(--blue)}
.delta{color:var(--red)}

.filterbar{left:396px;top:79px;width:782px;height:56px;background:var(--orange-hl)}
.filterbar .link{position:absolute;top:6px;color:#fff;font-size:10.5px;font-weight:700;text-decoration:underline}
.field{position:absolute;top:28px;height:20px;background:#fff;border-radius:10px;font-size:7.5px;color:var(--muted);padding:5px 12px}
.field.dim{color:#ddd}
.checkbox{position:absolute;left:436px;top:9px;width:10px;height:10px;background:#fff;border-radius:2px}
.divider{position:absolute;left:696px;top:6px;width:1px;height:44px;background:rgba(255,255,255,.5)}

.card{background:var(--card);box-shadow:0 1px 3px rgba(0,0,0,.15)}
.card h2{position:absolute;left:14px;top:12px;font-size:14px;font-weight:400;color:#111}
.card .date{position:absolute;top:12px;font-size:12.5px;color:#111;display:flex;align-items:center;gap:5px}
.pie{width:15px;height:15px;border-radius:50%;background:conic-gradient(#fff 0 25%,var(--orange-hl) 25% 100%);display:block}
.card svg{position:absolute;left:0;top:0}
svg text{font-family:'Lato',sans-serif}
.fill-card{background:linear-gradient(160deg,#fff 20%,#eef5e2 100%)}
</style>
</head>
<body>
<div class="app">
  <div class="abs topbar">
    <div class="abs brand"><i></i>VANTA</div>
    <div class="abs tab-capacity">⚖ Capacity</div>
    <div class="abs tab-more"><span class="dot"></span>More</div>
  </div>
  <nav class="abs navbar">
    <div class="nav-item active" style="left:32px">☰ Dashboard</div>
    <div class="nav-item" style="left:141px">💡 Lights</div>
    <div class="nav-item" style="left:218px"><span class="icon-box"></span>Daily Plan</div>
    <div class="nav-item" style="left:311px"><span class="icon-box"></span>Long Term Plan</div>
    <div class="nav-item" style="left:424px"><span class="icon-box"></span>Schedule Recommendation</div>
    <div class="nav-item" style="left:592px">⚙ Config</div>
  </nav>

  <aside class="abs panel-left">
    <div class="abs actions-label">Actions for</div>
    <div class="abs select">West Harbor Point</div>
    <div class="abs pill" style="left:2px;width:92px;background:var(--orange-hl)">Action Required (4)</div>
    <div class="abs pill" style="left:96px;width:94px;background:var(--orange)">Review Required (9)</div>
    <div class="abs days" style="left:11px">Today</div>
    <div class="abs days" style="left:117px">Tomorrow</div>
    <div class="abs days" style="left:218px">+2</div>
    <div class="abs days" style="left:322px">+3</div>
    <div class="abs day-line"></div><div class="abs day-ind"></div>
    <div class="abs dates" style="left:12px">03.12</div>
    <div class="abs dates" style="left:129px">03.13</div>
    <div class="abs dates" style="left:212px">03.14</div>
    <div class="abs dates" style="left:316px">03.15</div>

    <!-- site rows -->
    <div class="abs site closed" style="top:170px">
      <div class="abs accent"></div><div class="abs site-name">NSVL_PARIS_CB</div><div class="abs badge">CLOSED</div>
      <div class="abs metric boxed" style="left:18px;width:59px"><div class="title">In</div><div class="sub"><svg width="24" height="11" viewBox="0 0 24 11"><circle cx="4" cy="3" r="2.3" fill="#067ab4"/><path d="M0 11a4 4 0 018 0z" fill="#067ab4"/><circle cx="10" cy="3" r="2.3" fill="#067ab4"/><path d="M6 11a4 4 0 018 0z" fill="#067ab4"/><path d="M23 9c-2-4-5-5-8-5l2-2M15 4l2 2" stroke="#067ab4" stroke-width="1.5" fill="none"/></svg>+10</div></div>
      <div class="abs metric" style="left:84px;width:40px"><div class="title">Out</div><div class="sub"><svg width="26" height="11" viewBox="0 0 26 11"><path d="M1 9c2-4 5-5 8-5l-2-2M9 4l-2 2" stroke="#067ab4" stroke-width="1.5" fill="none"/><circle cx="14" cy="3" r="2.3" fill="#067ab4"/><path d="M10 11a4 4 0 018 0z" fill="#067ab4"/><circle cx="20" cy="3" r="2.3" fill="#067ab4"/><path d="M16 11a4 4 0 018 0z" fill="#067ab4"/></svg></div></div>
      <div class="abs metric boxed" style="left:123px;width:77px"><div class="title">Auth&nbsp; OT</div><div class="sub"><svg width="18" height="16" viewBox="0 0 18 16"><path d="M3 14A7 7 0 1115 14" stroke="#067ab4" stroke-width="1.5" fill="none"/><path d="M9 10l4-5" stroke="#067ab4" stroke-width="1.5"/></svg>120 mints</div></div>
      <div class="abs metric" style="left:206px;width:76px"><div class="title">Avail Rsv Cap</div><div class="cap-bar" style="left:8px"><i style="width:100%"></i></div></div>
      <div class="abs metric boxed" style="left:285px;width:77px"><div class="title">Supply Delta</div><div class="sub"><svg width="24" height="13" viewBox="0 0 24 13"><path d="M1 1v11h22z" fill="#067ab4"/><path d="M5 6v6h6z" fill="#fff"/></svg><span class="delta">-3,930</span></div></div>
    </div>

    <div class="abs site closed" style="top:271px">
      <div class="abs accent"></div><div class="abs site-name">NSVL_PARIS_CB</div><div class="abs badge">CLOSED</div>
      <div class="abs metric boxed" style="left:18px;width:59px"><div class="title">In</div><div class="sub"><svg width="24" height="11" viewBox="0 0 24 11"><circle cx="4" cy="3" r="2.3" fill="#067ab4"/><path d="M0 11a4 4 0 018 0z" fill="#067ab4"/><circle cx="10" cy="3" r="2.3" fill="#067ab4"/><path d="M6 11a4 4 0 018 0z" fill="#067ab4"/><path d="M23 9c-2-4-5-5-8-5l2-2M15 4l2 2" stroke="#067ab4" stroke-width="1.5" fill="none"/></svg>+10</div></div>
      <div class="abs metric" style="left:84px;width:40px"><div class="title">Out</div><div class="sub"><svg width="26" height="11" viewBox="0 0 26 11"><path d="M1 9c2-4 5-5 8-5l-2-2M9 4l-2 2" stroke="#067ab4" stroke-width="1.5" fill="none"/><circle cx="14" cy="3" r="2.3" fill="#067ab4"/><path d="M10 11a4 4 0 018 0z" fill="#067ab4"/><circle cx="20" cy="3" r="2.3" fill="#067ab4"/><path d="M16 11a4 4 0 018 0z" fill="#067ab4"/></svg></div></div>
      <div class="abs metric boxed" style="left:123px;width:77px"><div class="title">Auth&nbsp; OT</div><div class="sub"><svg width="18" height="16" viewBox="0 0 18 16"><path d="M3 14A7 7 0 1115 14" stroke="#067ab4" stroke-width="1.5" fill="none"/><path d="M9 10l4-5" stroke="#067ab4" stroke-width="1.5"/></svg>120 mints</div></div>
      <div class="abs metric" style="left:206px;width:76px"><div class="title">Avail Rsv Cap</div><div class="cap-bar" style="left:8px"><i style="width:100%"></i></div></div>
      <div class="abs metric boxed" style="left:285px;width:77px"><div class="title">Supply Delta</div><div class="sub"><svg width="24" height="13" viewBox="0 0 24 13"><path d="M1 1v11h22z" fill="#067ab4"/><path d="M5 6v6h6z" fill="#fff"/></svg><span class="delta">-3,930</span></div></div>
    </div>

    <div class="abs site open" style="top:372px">
      <div class="abs accent"></div><div class="abs site-name">NSVL_PARIS_CB</div><div class="abs badge">OPEN</div>
      <div class="abs metric boxed" style="left:18px;width:59px"><div class="title">In</div><div class="sub"><svg width="24" height="11" viewBox="0 0 24 11"><circle cx="4" cy="3" r="2.3" fill="#067ab4"/><path d="M0 11a4 4 0 018 0z" fill="#067ab4"/><circle cx="10" cy="3" r="2.3" fill="#067ab4"/><path d="M6 11a4 4 0 018 0z" fill="#067ab4"/><path d="M23 9c-2-4-5-5-8-5l2-2M15 4l2 2" stroke="#067ab4" stroke-width="1.5" fill="none"/></svg>+10</div></div>
      <div class="abs metric" style="left:84px;width:40px"><div class="title">Out</div><div class="sub"><svg width="26" height="11" viewBox="0 0 26 11"><path d="M1 9c2-4 5-5 8-5l-2-2M9 4l-2 2" stroke="#067ab4" stroke-width="1.5" fill="none"/><circle cx="14" cy="3" r="2.3" fill="#067ab4"/><path d="M10 11a4 4 0 018 0z" fill="#067ab4"/><circle cx="20" cy="3" r="2.3" fill="#067ab4"/><path d="M16 11a4 4 0 018 0z" fill="#067ab4"/></svg></div></div>
      <div class="abs metric boxed" style="left:123px;width:77px"><div class="title">Auth&nbsp; OT</div><div class="sub"><svg width="18" height="16" viewBox="0 0 18 16"><path d="M3 14A7 7 0 1115 14" stroke="#067ab4" stroke-width="1.5" fill="none"/><path d="M9 10l4-5" stroke="#067ab4" stroke-width="1.5"/></svg>120 mints</div></div>
      <div class="abs metric" style="left:206px;width:76px"><div class="title">Avail Rsv Cap</div><div class="cap-bar" style="left:8px"><i style="width:100%"></i></div></div>
      <div class="abs metric boxed" style="left:285px;width:77px"><div class="title">Supply Delta</div><div class="sub"><svg width="24" height="13" viewBox="0 0 24 13"><path d="M1 1v11h22z" fill="#067ab4"/><path d="M5 6v6h6z" fill="#fff"/></svg><span class="delta">-3,930</span></div></div>
    </div>

    <div class="abs site open" style="top:473px">
      <div class="abs accent"></div><div class="abs site-name">NSVL_PARIS_CB</div><div class="abs badge">OPEN</div>
      <div class="abs metric boxed" style="left:18px;width:59px"><div class="title">In</div><div class="sub"><svg width="24" height="11" viewBox="0 0 24 11"><circle cx="4" cy="3" r="2.3" fill="#067ab4"/><path d="M0 11a4 4 0 018 0z" fill="#067ab4"/><circle cx="10" cy="3" r="2.3" fill="#067ab4"/><path d="M6 11a4 4 0 018 0z" fill="#067ab4"/><path d="M23 9c-2-4-5-5-8-5l2-2M15 4l2 2" stroke="#067ab4" stroke-width="1.5" fill="none"/></svg>+10</div></div>
      <div class="abs metric" style="left:84px;width:40px"><div class="title">Out</div><div class="sub"><svg width="26" height="11" viewBox="0 0 26 11"><path d="M1 9c2-4 5-5 8-5l-2-2M9 4l-2 2" stroke="#067ab4" stroke-width="1.5" fill="none"/><circle cx="14" cy="3" r="2.3" fill="#067ab4"/><path d="M10 11a4 4 0 018 0z" fill="#067ab4"/><circle cx="20" cy="3" r="2.3" fill="#067ab4"/><path d="M16 11a4 4 0 018 0z" fill="#067ab4"/></svg></div></div>
      <div class="abs metric boxed" style="left:123px;width:77px"><div class="title">Auth&nbsp; OT</div><div class="sub"><svg width="18" height="16" viewBox="0 0 18 16"><path d="M3 14A7 7 0 1115 14" stroke="#067ab4" stroke-width="1.5" fill="none"/><path d="M9 10l4-5" stroke="#067ab4" stroke-width="1.5"/></svg>120 mints</div></div>
      <div class="abs metric" style="left:206px;width:76px"><div class="title">Avail Rsv Cap</div><div class="cap-bar" style="left:8px"><i style="width:100%"></i></div></div>
      <div class="abs metric boxed" style="left:285px;width:77px"><div class="title">Supply Delta</div><div class="sub"><svg width="24" height="13" viewBox="0 0 24 13"><path d="M1 1v11h22z" fill="#067ab4"/><path d="M5 6v6h6z" fill="#fff"/></svg><span class="delta">-3,930</span></div></div>
    </div>

    <div class="abs site open" style="top:575px">
      <div class="abs accent"></div><div class="abs site-name">NSVL_PARIS_CB</div><div class="abs badge">OPEN</div>
      <div class="abs metric boxed" style="left:18px;width:59px"><div class="title">In</div><div class="sub"><svg width="24" height="11" viewBox="0 0 24 11"><circle cx="4" cy="3" r="2.3" fill="#067ab4"/><path d="M0 11a4 4 0 018 0z" fill="#067ab4"/><circle cx="10" cy="3" r="2.3" fill="#067ab4"/><path d="M6 11a4 4 0 018 0z" fill="#067ab4"/><path d="M23 9c-2-4-5-5-8-5l2-2M15 4l2 2" stroke="#067ab4" stroke-width="1.5" fill="none"/></svg>+10</div></div>
      <div class="abs metric" style="left:84px;width:40px"><div class="title">Out</div><div class="sub"><svg width="26" height="11" viewBox="0 0 26 11"><path d="M1 9c2-4 5-5 8-5l-2-2M9 4l-2 2" stroke="#067ab4" stroke-width="1.5" fill="none"/><circle cx="14" cy="3" r="2.3" fill="#067ab4"/><path d="M10 11a4 4 0 018 0z" fill="#067ab4"/><circle cx="20" cy="3" r="2.3" fill="#067ab4"/><path d="M16 11a4 4 0 018 0z" fill="#067ab4"/></svg></div></div>
      <div class="abs metric boxed" style="left:123px;width:77px"><div class="title">Auth&nbsp; OT</div><div class="sub"><svg width="18" height="16" viewBox="0 0 18 16"><path d="M3 14A7 7 0 1115 14" stroke="#067ab4" stroke-width="1.5" fill="none"/><path d="M9 10l4-5" stroke="#067ab4" stroke-width="1.5"/></svg>120 mints</div></div>
      <div class="abs metric" style="left:206px;width:76px"><div class="title">Avail Rsv Cap</div><div class="cap-bar" style="left:8px"><i style="width:100%"></i></div></div>
      <div class="abs metric boxed" style="left:285px;width:77px"><div class="title">Supply Delta</div><div class="sub"><svg width="24" height="13" viewBox="0 0 24 13"><path d="M1 1v11h22z" fill="#067ab4"/><path d="M5 6v6h6z" fill="#fff"/></svg><span class="delta">-3,930</span></div></div>
    </div>
  </aside>

  <section class="abs filterbar">
    <span class="link" style="left:9px">Previously Viewed</span>
    <div class="field" style="left:8px;width:306px">NSVL_PARIS_CB<span style="position:absolute;right:10px;top:3px;font-size:9px">⇕</span></div>
    <span class="link" style="left:297px">Today</span>
    <div class="field" style="left:295px;width:136px">19.03.2018<span style="position:absolute;right:8px;top:3px;font-size:9px">▦</span></div>
    <span class="checkbox"></span>
    <span class="link" style="left:450px">Show date range</span>
    <div class="field dim" style="left:431px;width:108px">19.03.2018<span style="position:absolute;right:8px;top:3px;font-size:9px">▦</span></div>
    <svg class="abs" style="left:635px;top:14px" width="32" height="28" viewBox="0 0 32 28"><g fill="none" stroke="#fff" stroke-width="2"><path d="M1 27h30"/><rect x="3" y="12" width="5" height="15"/><rect x="10" y="6" width="5" height="21"/><rect x="17" y="14" width="5" height="13"/><rect x="24" y="3" width="5" height="24"/></g></svg>
    <div class="divider"></div>
    <svg class="abs" style="left:730px;top:11px" width="34" height="34" viewBox="0 0 34 34"><path d="M15 3a15 15 0 1016 16H15z" fill="#fff"/><path d="M18 0a16 16 0 0116 16H18z" fill="#fff"/></svg>
  </section>

  <!-- line chart -->
  <section class="abs card" style="left:398px;top:156px;width:384px;height:251px">
    <h2>Dashboard</h2>
    <svg width="384" height="251" viewBox="0 0 384 251">
      <path d="M44 162 L60 90 C80 120 100 140 122 125 C140 100 150 60 170 110 C190 140 210 130 230 110 C250 80 265 50 285 70 C300 90 310 120 330 130 C345 150 355 110 370 100 L370 162Z" fill="#e6f1d6"/>
      <g stroke="#eee"><line x1="34" y1="59" x2="370" y2="59"/><line x1="34" y1="85" x2="370" y2="85"/><line x1="34" y1="111" x2="370" y2="111"/><line x1="34" y1="136" x2="370" y2="136"/><line x1="34" y1="162" x2="370" y2="162" stroke="#ccc"/></g>
      <g font-size="7" fill="#555" text-anchor="end"><text x="22" y="61">125</text><text x="22" y="87">100</text><text x="22" y="113">75</text><text x="22" y="138">50</text><text x="22" y="164">25</text></g>
      <polyline fill="none" stroke="#777" stroke-width="1" points="55,162 70,100 95,110 115,155 140,112 160,70 185,118 200,92 230,112 255,90 285,142 310,122 325,160 345,122 363,135"/>
      <polyline fill="none" stroke="#81017e" stroke-width="1" points="60,77 85,88 104,47 128,74 150,66 172,92 190,80 210,107 230,117 248,96 265,116 285,73"/>
      <polyline fill="none" stroke="#b30a3c" stroke-width="1.2" points="57,162 75,125 100,85 118,116 133,57 155,92 175,116 190,163 208,110 228,122 248,130 270,90 288,113 300,100 320,62"/>
      <polyline fill="none" stroke="#2a9d16" stroke-width="1.2" points="36,135 57,85 78,106 102,75 120,60 140,35 158,93 178,110 200,95 220,103 240,115 262,120 272,93 292,35"/>
      <g font-size="5.5" fill="#555"><text x="28" y="172">27.2.2018</text><text x="62" y="172">27.2.2018</text><text x="96" y="172">27.2.2018</text><text x="130" y="172">27.2.2018</text><text x="164" y="172">27.2.2018</text><text x="198" y="172">27.2.2018</text><text x="232" y="172">27.2.2018</text><text x="266" y="172">27.2.2018</text><text x="300" y="172">27.2.2018</text><text x="334" y="172">27.2.2018</text>
        <text x="38" y="183">27.2.2018</text><text x="72" y="183">27.2.2018</text><text x="106" y="183">27.2.2018</text><text x="140" y="183">27.2.2018</text><text x="174" y="183">27.2.2018</text><text x="208" y="183">27.2.2018</text><text x="242" y="183">27.2.2018</text><text x="276" y="183">27.2.2018</text><text x="310" y="183">27.2.2018</text><text x="344" y="183">27.2.2018</text></g>
      <g font-size="8.5" fill="#333"><circle cx="23" cy="212" r="2.3" fill="#b30a3c"/><text x="29" y="215">Install Intakes</text><circle cx="101" cy="212" r="2.3" fill="#555"/><text x="107" y="215">Install Completions</text><circle cx="198" cy="212" r="2.3" fill="#81017e"/><text x="204" y="215">Repair Intakes</text><circle cx="275" cy="212" r="2.3" fill="#2a9d16"/><text x="281" y="215">Repair Completions</text></g>
    </svg>
  </section>

  <!-- tech breakdown 1 -->
  <section class="abs card" style="left:791px;top:156px;width:389px;height:251px">
    <h2>Technian Breakdown</h2>
    <svg width="389" height="251" viewBox="0 0 389 251">
      <g stroke="#ddd"><line x1="98" y1="33" x2="98" y2="221"/><line x1="128" y1="33" x2="128" y2="221"/><line x1="158" y1="33" x2="158" y2="221"/><line x1="188" y1="33" x2="188" y2="221"/><line x1="218" y1="33" x2="218" y2="221"/><line x1="248" y1="33" x2="248" y2="221"/><line x1="278" y1="33" x2="278" y2="221"/><line x1="308" y1="33" x2="308" y2="221"/><line x1="338" y1="33" x2="338" y2="221"/><line x1="367" y1="33" x2="367" y2="221"/></g>
      <g font-size="8" fill="#555" text-anchor="end"><text x="86" y="53">Available Techs</text><text x="86" y="73">Techs On Proactive</text><text x="86" y="83">Load</text><text x="86" y="109">Loan Out</text><text x="86" y="142">Loan In</text><text x="86" y="172">Assigned to Load</text><text x="86" y="199">Usheduled Techs</text><text x="86" y="219">Scheduled Techs</text></g>
      <g stroke-linecap="round" stroke-width="4">
        <line x1="98" y1="50" x2="128" y2="50" stroke="#ff7200"/>
        <line x1="98" y1="71" x2="152" y2="71" stroke="#3aa5dc"/>
        <line x1="98" y1="92" x2="104" y2="92" stroke="#067ab4"/>
        <line x1="98" y1="110" x2="99" y2="110" stroke="#067ab4"/>
        <line x1="98" y1="139" x2="208" y2="139" stroke="#3aa5dc"/>
        <line x1="98" y1="145" x2="224" y2="145" stroke="#ff7200"/>
        <line x1="98" y1="168" x2="120" y2="168" stroke="#ff7200"/>
        <line x1="98" y1="174" x2="116" y2="174" stroke="#3aa5dc"/>
        <line x1="98" y1="209" x2="310" y2="209" stroke="#ff7200"/>
        <line x1="98" y1="215" x2="230" y2="215" stroke="#3aa5dc"/>
      </g>
      <g font-size="8" fill="#555" text-anchor="middle"><text x="98" y="233">0</text><text x="128" y="233">20</text><text x="158" y="233">40</text><text x="188" y="233">60</text><text x="218" y="233">80</text><text x="248" y="233">100</text><text x="278" y="233">120</text><text x="308" y="233">140</text><text x="338" y="233">160</text><text x="367" y="233">180</text></g>
    </svg>
  </section>

  <!-- fill rate -->
  <section class="abs card fill-card" style="left:398px;top:417px;width:384px;height:198px">
    <h2>Fill Rate</h2>
    <div class="date" style="left:294px"><span class="pie"></span>19.03.2018</div>
    <svg width="384" height="198" viewBox="0 0 384 198">
      <defs><linearGradient id="ringOrange" x1="0" y1="0" x2="0" y2="1"><stop offset="0" stop-color="#ff7200"/><stop offset="1" stop-color="#fcb314"/></linearGradient>
      <linearGradient id="ringBlue" x1="0" y1="1" x2="1" y2="0"><stop offset="0" stop-color="#eaab00"/><stop offset=".5" stop-color="#6b8a9c"/><stop offset="1" stop-color="#067ab4"/></linearGradient></defs>
      <circle cx="94" cy="117" r="62" fill="#f3f3f3"/>
      <path d="M99 47 A70 70 0 0 1 136 173" fill="none" stroke="#ff7200" stroke-width="11"/>
      <path d="M130 177 A70 70 0 0 1 29 135" fill="none" stroke="url(#ringOrange)" stroke-width="11"/>
      <path d="M27 128 A70 70 0 0 1 88 47" fill="none" stroke="url(#ringBlue)" stroke-width="11"/>
      <text x="94" y="133" font-size="36" fill="#222" text-anchor="middle">112%</text>
      <path d="M204 104 l6 -10 l6 10z" fill="none" stroke="#22a012" stroke-width="1.5"/>
      <text x="222" y="104" font-size="12" fill="#333">5.1%</text>
    </svg>
  </section>

  <!-- tech breakdown 2 -->
  <section class="abs card" style="left:791px;top:417px;width:389px;height:196px">
    <h2>Technian Breakdown</h2>
    <svg width="389" height="196" viewBox="0 0 389 196">
      <g stroke="#ddd"><line x1="98" y1="46" x2="98" y2="156"/><line x1="128" y1="46" x2="128" y2="156"/><line x1="158" y1="46" x2="158" y2="156"/><line x1="188" y1="46" x2="188" y2="156"/><line x1="218" y1="46" x2="218" y2="156"/><line x1="248" y1="46" x2="248" y2="156"/><line x1="278" y1="46" x2="278" y2="156"/><line x1="308" y1="46" x2="308" y2="156"/><line x1="338" y1="46" x2="338" y2="156"/><line x1="367" y1="46" x2="367" y2="156"/></g>
      <g font-size="8" fill="#555" text-anchor="end"><text x="85" y="67">Available Techs</text><text x="85" y="89">Techs On Proactive</text><text x="85" y="98">Work</text><text x="85" y="126">Techs On loads</text><text x="85" y="150">Activates Techs</text></g>
      <g stroke-linecap="round" stroke-width="4">
        <line x1="98" y1="64" x2="128" y2="64" stroke="#81017e"/>
        <line x1="98" y1="92" x2="152" y2="92" stroke="#067ab4"/>
        <line x1="98" y1="120" x2="208" y2="120" stroke="#3aa5dc"/>
        <line x1="98" y1="126" x2="224" y2="126" stroke="#b8509e"/>
        <line x1="98" y1="142" x2="310" y2="142" stroke="#b8509e"/>
        <line x1="98" y1="148" x2="230" y2="148" stroke="#3aa5dc"/>
      </g>
      <g font-size="8" fill="#555" text-anchor="middle"><text x="98" y="166">0</text><text x="128" y="166">20</text><text x="158" y="166">40</text><text x="188" y="166">60</text><text x="218" y="166">80</text><text x="248" y="166">100</text><text x="278" y="166">120</text><text x="308" y="166">140</text><text x="338" y="166">160</text><text x="367" y="166">180</text></g>
      <g font-size="8.5" fill="#333"><circle cx="135" cy="183" r="2.3" fill="#81017e"/><text x="140" y="186">TFS</text><circle cx="212" cy="183" r="2.3" fill="#067ab4"/><text x="217" y="186">IEFS</text></g>
    </svg>
  </section>

  <!-- installs / repairs -->
  <section class="abs card" style="left:398px;top:625px;width:198px;height:200px">
    <h2>Installs</h2>
    <h2 style="left:130px">Repairs</h2>
    <svg width="198" height="200" viewBox="0 0 198 200">
      <defs>
        <linearGradient id="gPurple" x1="0" y1="0" x2="0" y2="1"><stop offset="0" stop-color="#b8509e"/><stop offset="1" stop-color="#81017e"/></linearGradient>
        <linearGradient id="gOrange" x1="0" y1="0" x2="0" y2="1"><stop offset="0" stop-color="#ff9900"/><stop offset="1" stop-color="#ff3d00"/></linearGradient>
      </defs>
      <g stroke="#ddd"><line x1="20" y1="47" x2="70" y2="47"/><line x1="20" y1="67" x2="70" y2="67"/><line x1="20" y1="88" x2="70" y2="88"/><line x1="20" y1="109" x2="70" y2="109"/><line x1="20" y1="130" x2="70" y2="130"/>
        <line x1="130" y1="47" x2="180" y2="47"/><line x1="130" y1="67" x2="180" y2="67"/><line x1="130" y1="88" x2="180" y2="88"/><line x1="130" y1="109" x2="180" y2="109"/><line x1="130" y1="130" x2="180" y2="130"/></g>
      <g font-size="7.5" fill="#555" text-anchor="end"><text x="18" y="50">120</text><text x="18" y="70">110</text><text x="18" y="91">100</text><text x="18" y="112">90</text><text x="18" y="133">80</text>
        <text x="127" y="50">120</text><text x="127" y="70">110</text><text x="127" y="91">100</text><text x="127" y="112">90</text><text x="127" y="133">80</text></g>
      <rect x="30" y="78" width="9" height="52" rx="4" fill="url(#gPurple)"/>
      <rect x="52" y="66" width="9" height="64" rx="4" fill="url(#gOrange)"/>
      <rect x="139" y="78" width="9" height="52" rx="4" fill="url(#gPurple)"/>
      <rect x="161" y="66" width="9" height="64" rx="4" fill="url(#gOrange)"/>
      <g font-size="8.5" fill="#333"><circle cx="47" cy="159" r="2.3" fill="#81017e"/><text x="52" y="162">TFS</text><circle cx="124" cy="159" r="2.3" fill="#ff3d00"/><text x="130" y="162">IEFS</text></g>
    </svg>
  </section>

  <!-- duration -->
  <section class="abs card" style="left:622px;top:625px;width:199px;height:200px">
    <h2>Duration</h2>
    <div class="date" style="left:108px"><span class="pie"></span>19.03.2018</div>
    <svg width="199" height="200" viewBox="0 0 199 200">
      <defs>
        <linearGradient id="gAmber" x1="0" y1="0" x2="0" y2="1"><stop offset="0" stop-color="#fcb314"/><stop offset="1" stop-color="#ff7200"/></linearGradient>
        <linearGradient id="gBlue" x1="0" y1="0" x2="0" y2="1"><stop offset="0" stop-color="#067ab4"/><stop offset="1" stop-color="#3aa5dc"/></linearGradient>
      </defs>
      <g stroke="#ddd"><line x1="24" y1="47" x2="185" y2="47"/><line x1="24" y1="67" x2="185" y2="67"/><line x1="24" y1="88" x2="185" y2="88"/><line x1="24" y1="109" x2="185" y2="109"/><line x1="24" y1="130" x2="185" y2="130"/></g>
      <g font-size="7.5" fill="#555" text-anchor="end"><text x="20" y="50">120</text><text x="20" y="70">110</text><text x="20" y="91">100</text><text x="20" y="112">90</text><text x="20" y="133">80</text></g>
      <rect x="52" y="78" width="9" height="52" rx="4" fill="url(#gAmber)"/>
      <rect x="75" y="66" width="9" height="64" rx="4" fill="url(#gBlue)"/>
      <g font-size="8.5" fill="#333" text-anchor="middle"><text x="58" y="162">Mints</text><text x="97" y="162">Install</text><text x="138" y="162">Repair</text></g>
    </svg>
  </section>

  <!-- tech commit -->
  <section class="abs card" style="left:844px;top:625px;width:199px;height:200px">
    <h2>Tech Commit</h2>
    <div class="date" style="left:108px"><span class="pie"></span>19.03.2018</div>
    <svg width="199" height="200" viewBox="0 0 199 200">
      <defs>
        <linearGradient id="gRed" x1="0" y1="0" x2="0" y2="1"><stop offset="0" stop-color="#ff0066"/><stop offset="1" stop-color="#b30a3c"/></linearGradient>
        <linearGradient id="gBlue2" x1="0" y1="0" x2="0" y2="1"><stop offset="0" stop-color="#067ab4"/><stop offset="1" stop-color="#3aa5dc"/></linearGradient>
      </defs>
      <g stroke="#ddd"><line x1="24" y1="47" x2="185" y2="47"/><line x1="24" y1="67" x2="185" y2="67"/><line x1="24" y1="88" x2="185" y2="88"/><line x1="24" y1="109" x2="185" y2="109"/><line x1="24" y1="130" x2="185" y2="130"/></g>
      <g font-size="7.5" fill="#555" text-anchor="end"><text x="20" y="50">120</text><text x="20" y="70">110</text><text x="20" y="91">100</text><text x="20" y="112">90</text><text x="20" y="133">80</text></g>
      <rect x="53" y="78" width="9" height="52" rx="4" fill="url(#gRed)"/>
      <rect x="76" y="66" width="9" height="64" rx="4" fill="url(#gBlue2)"/>
      <g font-size="8.5" fill="#333" text-anchor="middle"><text x="59" y="162">Mints</text><text x="98" y="162">Install</text><text x="139" y="162">Repair</text></g>
    </svg>
  </section>
</div>
</body>
</html>
```